ALL TEXT Social Media Graphics

We are looking for a series of social media graphics for Instagram (new size: 4:5 (1080 x 1350 pixels) ratio that are ALL TEXT. We want the following quotes below on each graphic; one quote per graphic. AND, In very small letters at the bottom of each graphic, add @PaulaWrenLive
The look and feel of these graphics should be complimentary to the color palette attached below; but keep them simple. But the design is up to you; at the end of this document, I provided various samples of all text graphics that I like as examples.
The Quotes are in the attached WORD document
women trying to lose weight

```html
<!DOCTYPE html>
<html lang="en">
<head>
<meta charset="utf-8">
<title>Golden Girl Summer Slimdown</title>
<link href="https://fonts.googleapis.com/css2?family=Bebas+Neue&family=Arimo:wght@700&display=swap" rel="stylesheet">
<style>
  :root {
    --berry: #a8164f;
    --rose: #ee6095;
    --blush: #fbc0e2;
    --ink: #050505;
    --white: #ffffff;
    --bg-deep: #b3265e;
    --bg-mid: #da87a3;
    --bg-soft: #f4d3de;
  }
  * { margin: 0; padding: 0; box-sizing: border-box; }
  html, body { width: 960px; height: 1200px; overflow: hidden; }
  body { font-family: "Bebas Neue", Impact, sans-serif; }
  .post {
    position: relative;
    width: 960px;
    height: 1200px;
    overflow: hidden;
    background: linear-gradient(38deg, var(--bg-deep) 0%, var(--bg-mid) 38%, var(--bg-soft) 66%, var(--white) 92%);
  }
  .line {
    position: absolute;
    left: 55px;
    line-height: 1;
    white-space: nowrap;
  }
  .headline-lead { top: 160px; font-size: 89px; color: var(--berry); }
  .headline-lead em { font-style: italic; }
  .headline-need { top: 266px; font-size: 121px; color: var(--berry); }
  .system-band {
    position: absolute;
    left: 55px; top: 395px;
    width: 852px; height: 141px;
    background: var(--rose);
  }
  .system-text {
    position: absolute;
    left: 23px; top: 20px;
    font-size: 124px; line-height: 1;
    color: var(--white);
    white-space: nowrap;
  }
  .offer { top: 564px; font-size: 124px; color: var(--ink); }
  .offer-with { top: 691px; font-size: 84px; color: var(--blush); }
  .program { top: 791px; left: 60px; font-size: 83px; color: var(--ink); }
  .cta { top: 990px; left: 53px; font-size: 51px; color: var(--white); }
  .cta em { font-style: italic; }
  .handle {
    position: absolute;
    left: 55px; top: 1103px;
    font-family: "Arimo", Arial, sans-serif;
    font-weight: 700;
    font-size: 22px;
    color: var(--white);
  }
</style>
</head>
<body>
  <main class="post">
    <p class="line headline-lead">You don’t need <em>another diet</em></p>
    <p class="line headline-need">You need a</p>
    <div class="system-band"><p class="system-text">System that works.</p></div>
    <p class="line offer">Drop 30 pounds</p>
    <p class="line offer-with">With the</p>
    <p class="line program">Golden Girl Summer Slimdown.</p>
    <p class="line cta">Comment <em>“Summer”</em> to start now.</p>
    <p class="handle">@PaulaWrenLive</p>
  </main>
</body>
</html>
```